B2B modern industry lubrication label

We are a chemical company that needs a new, very modern outstanding lubrication packaging label. The logo attached can be changed in color. The name of the product is R83. Attached also the text you can use, please disregard the current layout of the text, you can make it any layout you want. Be free in font type, colors and other design aspects.
Dimensions: 21 x 14,8 cm
industry, companies with machinery
Industrial

```html
<!DOCTYPE html>
<html lang="en">
<head>
<meta charset="utf-8">
<title>R83 Pro Spray Label</title>
<link rel="stylesheet" href="https://fonts.googleapis.com/css2?family=Figtree:wght@400;600;800&display=swap">
<style>
  :root {
    --brand-orange: #ee5000;
    --brand-orange-soft: #f47a3a;
    --paper: #ffffff;
    --ink: #4a4a4a;
    --backdrop: #e4e2e2;
  }
  * { margin: 0; padding: 0; box-sizing: border-box; }
  html, body {
    width: 1200px; height: 1200px; overflow: hidden;
    background: var(--backdrop);
    font-family: "Figtree", Arial, sans-serif;
  }
  .label {
    position: absolute; left: 28px; top: 256px;
    width: 1144px; height: 688px;
    background: var(--paper);
    border: 8px solid var(--brand-orange);
    border-bottom: none;
    overflow: hidden;
  }
  .label__decor {
    position: absolute; left: -8px; right: -8px; bottom: 0;
    height: 130px;
    background: linear-gradient(180deg, var(--brand-orange-soft) 0%, var(--brand-orange) 60%);
  }
  .label__content { position: absolute; inset: 0; }
  .brand-name {
    position: absolute; top: 32px; left: 0; right: 0;
    text-align: center;
    font-weight: 800; font-size: 128px; line-height: 1;
    letter-spacing: -3px;
    color: var(--brand-orange);
  }
  .product-title {
    position: absolute; top: 166px; left: 0; right: 0;
    text-align: center; font-weight: 600; font-size: 31px; line-height: 1;
    color: var(--brand-orange);
  }
  .section-heading {
    font-weight: 600; font-size: 20px; color: var(--brand-orange);
    line-height: 1;
  }
  .application { position: absolute; top: 218px; left: 42px; right: 42px; text-align: center; }
  .application p {
    margin-top: 16px; font-size: 11.8px; line-height: 15.4px; color: var(--ink);
  }
  .column { position: absolute; top: 358px; width: 470px; }
  .column--instructions { left: 66px; }
  .column--advantages { left: 544px; width: 490px; }
  .bullets { list-style: none; margin-top: 26px; }
  .bullets li {
    position: relative; padding-left: 19px;
    font-size: 11.8px; line-height: 15.3px; color: var(--ink);
  }
  .bullets li::before {
    content: ""; position: absolute; left: 0; top: 4px;
    width: 7px; height: 7px; border-radius: 50%;
    background: var(--brand-orange);
  }
</style>
</head>
<body>
  <div class="label">
    <div class="label__decor" role="img" aria-label="Flowing orange and white decorative wave band along the bottom of the label"></div>

    <div class="label__content">
      <div class="brand-name">KARVEN</div>
      <h1 class="product-title">R83 PRO (SPRAY)</h1>

      <section class="application">
        <h2 class="section-heading">APPLICATION:</h2>
        <p>R83 Pro is a high grade multifunctional product for lubrication and protection product.<br>
        R83 Pro is composed out of high grade synthetic oils, E.P. additives and penetrants. Also the product contains rust-preventing and waterproof substances. Practical experience proofed that R83 Pro cleans, lubricates and protects equipment, hinges, cables, conveyer belts, chains and other moving parts in machines and device excellently. R83 Pro cleans fats, resins and rust on the surface of materials. R83 Pro create a good and durable lubrication. Even under circumstances with extreme pressure.<br>
        R83 Pro protects against moisture and rust.</p>
      </section>

      <section class="column column--instructions">
        <h2 class="section-heading">INSTRUCTIONS FOR USE:</h2>
        <ul class="bullets">
          <li>Short shake before use</li>
          <li>Spray a thin layer of R83 Pro on the surface.</li>
          <li>The product will come out as a white, fast disappearing foam.<br>Let R83 Pro do its work for a few minutes.</li>
          <li>Own evaluation for necessity and result.</li>
        </ul>
      </section>

      <section class="column column--advantages">
        <h2 class="section-heading">SPECIAL ADVANTAGES:</h2>
        <ul class="bullets">
          <li>R83 Pro drives off the eventually present moisture.</li>
          <li>R83 Pro can handle temperatures until 370˚C.</li>
          <li>R83 Pro reaches even the smallest corners. This is because of the<br>pressure of the spray, foaming and presence of high grade penetrants.</li>
          <li>R83 Pro forms an extremely thin and smooth layer of grease (Fw value: 0,1).</li>
          <li>R83 Pro helps prevent “pitting wear”.</li>
          <li>With use in propulsions, the starting couple will be lowered.</li>
        </ul>
      </section>
    </div>
  </div>
</body>
</html>
```